Attorney Business Card

I need a business card that looks professional yet modern. I am an Attorney. , I need a professional yet modern business card for my law practice. My logo and information have been uploaded. , I need a business card that looks professional yet modern. I am an Attorney. , I need a professional yet modern business card for my law practice. My logo and information have been uploaded.

Industry/Entity Type

Business

Requirements
Must have
• My logo which has been uploaded , my logo , My logo which has been uploaded , my logo

```html
<!DOCTYPE html>
<html lang="en">
<head>
<meta charset="utf-8">
<title>Daniel Marchetti, Esq. – Business Card</title>
<link rel="stylesheet" href="https://fonts.googleapis.com/css2?family=Barlow:wght@400;500;700&display=swap">
<style>
  :root {
    --brand-blue: #29abe2;
    --brand-blue-faint: #e6f4fb;
    --card-white: #ffffff;
    --divider: #9fd3ee;
  }
  html, body {
    margin: 0;
    padding: 0;
    width: 1200px;
    height: 690px;
    overflow: hidden;
    background: var(--card-white);
  }
  .card {
    position: relative;
    width: 1200px;
    height: 690px;
    background: var(--card-white);
    font-family: "Barlow", "Helvetica Neue", Arial, sans-serif;
    color: var(--brand-blue);
    overflow: hidden;
  }
  .firm-mark {
    position: absolute;
    left: 0;
    width: 1200px;
    top: 150px;
    height: 280px;
    display: flex;
    justify-content: center;
    align-items: center;
    gap: 22px;
  }
  .firm-mark__dot {
    width: 36px;
    height: 36px;
    border-radius: 50%;
    background: var(--brand-blue-faint);
  }
  .firm-mark__name {
    font-size: 46px;
    font-weight: 500;
    letter-spacing: 2px;
    color: var(--brand-blue-faint);
    text-transform: uppercase;
    margin-top: -110px;
  }
  .firm-mark__dot { margin-top: -110px; }
  .name-band {
    position: absolute;
    left: 0;
    top: 271px;
    width: 1200px;
    height: 138px;
    background: var(--brand-blue);
    color: var(--card-white);
    text-align: center;
  }
  .name-band__name {
    position: absolute;
    left: 0; right: 0;
    top: 49px;
    transform: translateY(-50%);
    font-size: 45px;
    font-weight: 700;
    letter-spacing: 1.5px;
    line-height: 1;
  }
  .name-band__title {
    position: absolute;
    left: 0; right: 0;
    top: 99px;
    transform: translateY(-50%);
    font-size: 33px;
    font-weight: 400;
    line-height: 1;
  }
  .contact {
    position: absolute;
    display: flex;
    align-items: center;
    transform: translateY(-50%);
    font-size: 32px;
    font-weight: 400;
    line-height: 1;
    white-space: nowrap;
  }
  .contact svg {
    fill: var(--brand-blue);
    flex: none;
  }
  .contact--mobile { left: 133px; top: 483px; }
  .contact--office { left: 470px; top: 483px; }
  .contact--fax    { left: 812px; top: 483px; }
  .contact--email  { left: 128px; top: 561px; }
  .contact--web    { left: 128px; top: 605px; }
  .contact--mobile svg, .contact--office svg, .contact--fax svg { margin-right: 22px; }
  .contact--email svg, .contact--web svg { margin-right: 24px; }
  .divider {
    position: absolute;
    left: 523px;
    top: 543px;
    width: 2px;
    height: 89px;
    background: var(--divider);
  }
  .address {
    position: absolute;
    left: 575px;
    top: 548px;
    display: flex;
    align-items: flex-start;
  }
  .address svg { fill: var(--brand-blue); margin-right: 26px; margin-top: 4px; }
  .address__lines {
    font-size: 32px;
    line-height: 44px;
    font-style: normal;
  }
</style>
</head>
<body>
<div class="card">
  <div class="firm-mark">
    <span class="firm-mark__dot"></span>
    <span class="firm-mark__name">Marchetti Law Group</span>
  </div>

  <header class="name-band">
    <div class="name-band__name">DANIEL MARCHETTI, ESQ.</div>
    <div class="name-band__title">Attorney At Law</div>
  </header>

  <div class="contact contact--mobile">
    <svg width="20" height="30" viewBox="0 0 20 30" aria-hidden="true">
      <path d="M3 0h14a3 3 0 0 1 3 3v24a3 3 0 0 1-3 3H3a3 3 0 0 1-3-3V3a3 3 0 0 1 3-3zm0 4v19h14V4zm7 21a1.6 1.6 0 1 0 0 3.2A1.6 1.6 0 0 0 10 25z"/>
    </svg>
    <span>310.555.0142</span>
  </div>
  <div class="contact contact--office">
    <svg width="26" height="26" viewBox="0 0 24 24" aria-hidden="true">
      <path d="M6.6 10.8a15.1 15.1 0 0 0 6.6 6.6l2.2-2.2a1 1 0 0 1 1-.25 11.4 11.4 0 0 0 3.6.57 1 1 0 0 1 1 1V20a1 1 0 0 1-1 1A17 17 0 0 1 3 4a1 1 0 0 1 1-1h3.5a1 1 0 0 1 1 1 11.4 11.4 0 0 0 .57 3.6 1 1 0 0 1-.25 1z"/>
    </svg>
    <span>310.555.0170</span>
  </div>
  <div class="contact contact--fax">
    <svg width="28" height="24" viewBox="0 0 28 24" aria-hidden="true">
      <path d="M7 0h14v6H7zM3 8h22a3 3 0 0 1 3 3v8h-6v5H6v-5H0v-8a3 3 0 0 1 3-3zm6 8v6h10v-6zm14-5a1.5 1.5 0 1 0 0 3 1.5 1.5 0 0 0 0-3z"/>
    </svg>
    <span>310.555.0185</span>
  </div>

  <div class="contact contact--email">
    <svg width="26" height="19" viewBox="0 0 26 19" aria-hidden="true">
      <path d="M0 0h26v3L13 11 0 3zm0 6l13 8 13-8v13H0z"/>
    </svg>
    <span>daniel@mlawgroup.com</span>
  </div>
  <div class="contact contact--web">
    <svg width="26" height="26" viewBox="0 0 26 26" aria-hidden="true">
      <path d="M13 0a13 13 0 1 0 0 26 13 13 0 0 0 0-26zm-1 4c-2 1-4 3-5 5l3 2 1 3-2 2 1 4 3 1 1-4 3-3-2-3h-3l-1-2 2-1zm6 1l-1 3 3 2 2-1a10 10 0 0 0-4-4z"/>
    </svg>
    <span>www.mlawgroup.com</span>
  </div>

  <div class="divider"></div>

  <address class="address">
    <svg width="20" height="28" viewBox="0 0 20 28" aria-hidden="true">
      <path d="M10 0a10 10 0 0 0-10 10c0 7.5 10 18 10 18s10-10.5 10-18A10 10 0 0 0 10 0zm0 14a4 4 0 1 1 0-8 4 4 0 0 1 0 8z"/>
    </svg>
    <div class="address__lines">2210 Canyon Crest Blvd. Suite 400<br>Westfield, Ca 90418</div>
  </address>
</div>
</body>
</html>
```